Company brochure for our unique consulting business

We are a small consulting business offering a unique set of services to our clients.. In simple terms we are a business improvement consultancy helping our clients get the best out of their businesses. We work with clients across multiple sectors and deliver a variety of services. We want to put together a brochure to cover these main themes:1. Who we are2. What we do3. The type of people we employ4. The sectors we work inWhile the brochure needs to have a certain corporate feel to it, we don't want it to be "boring" or "stiff". We would like it to have a slightly "friendly" or "informal" feel to it, to reflect the type of organisation we are.We have a company website http://tollandvergeadvisory.com , however we do not want to directly replicate the content or feel as we recognise it needs updating.We would like the brochure to be A4 portrait format. We anticipate requiring 12 sides (including covers) but we are happy to be guided on this based on the content we have provided.The attached ppt file gives the detail of the content to be included and also shows the proposed pagination. For the front cover we would like to try 2 versions, one with the TVA logo and one with the Tolland Verge Advisory logo (a file of both is attached)One of the most important pages will be the "Our Services" page. We would like this to cover the centre fold. In the ppt file we have shown an example layout, but this is where we need most help - we are clearly not graphic designers! This page will be the most used page in sales meetings etc.Also attached is the following:1. file for our TollandVerge Advisory company logo.2. File for our TVA company logo3. Files for Derek's signatures (for under photos) - Owen's to follow4. Photo of Derek & Owen (person in purple shirt to be cropped out)Thank you and really excited to see what everyone comes back with.Derek & Owen

Target Market(s)

Very broad - Manufacturing, Healthcare, Hospitality

Industry/Entity Type

Management Consulting

Font styles to use
Other font styles liked:
• We use Swiss721, but happy to be guided by designer

Colors
3276b5
85abd2
0355a3
333333
5c5c5c
9d9d9d
d9d9d9

Requirements
Must have
• Corporate feel
Nice to have
• Slightly friendly feel
• Our standard "blue" is (CORRECTION) - R55 G96 B146 #376092 and our standard grey is R197 G178, B179 - #B3B2B2, which we would like to keep, but other colours we are happy to be guided on. Brand guidelines attached.

```html
<!DOCTYPE html>
<html lang="en">
<head>
<meta charset="utf-8">
<title>Tolland Verge Advisory – Brochure Covers</title>
<link href="https://fonts.googleapis.com/css2?family=Montserrat:wght@400;600;700&display=swap" rel="stylesheet">
<style>
  :root {
    --page-bg: #666666;
    --paper: #ffffff;
    --band: #f8fbfd;
    --halo: #eef4fb;
    --ring: #85abd2;
    --ring-light: #c3d6ec;
    --ring-thin: #cfdff0;
    --strip: #dce8f5;
    --heading: #1f3f99;
    --body: #6a6a6a;
    --icon: #85abd2;
    --link: #6f99cb;
    --brand: #376092;
  }
  * { margin: 0; padding: 0; box-sizing: border-box; }
  html, body { width: 1200px; height: 1200px; overflow: hidden; background: var(--page-bg); }
  body { font-family: "Montserrat", Arial, sans-serif; }
  .spread {
    position: absolute; left: 63px; top: 173px;
    width: 1078px; height: 762px; background: var(--paper); overflow: hidden;
    box-shadow: 0 20px 40px rgba(0,0,0,0.25);
  }
  .spread-art { position: absolute; left: 0; top: 0; }
  .contact { position: absolute; left: 34px; top: 526px; color: var(--body); }
  .contact-title { font-size: 16.5px; font-weight: 700; color: var(--heading); margin-bottom: 8px; }
  .contact-row { display: flex; align-items: flex-start; gap: 8px; font-size: 11.8px; line-height: 13.6px; margin-bottom: 6px; }
  .contact-row svg { flex: none; width: 13px; height: 13px; margin-top: 1px; }
  .contact-row.tight { margin-bottom: 2px; }
  .web-link { position: absolute; left: 34px; top: 681px; font-size: 9.6px; font-weight: 700; color: var(--link); }
  .brand-name {
    position: absolute; left: 787px; top: 618px;
    font-size: 34px; font-weight: 600; line-height: 37px; color: var(--brand); letter-spacing: -0.5px;
  }
</style>
</head>
<body>
<div class="spread">
  <svg class="spread-art" width="1078" height="762" viewBox="0 0 1078 762">
    <defs>
      <clipPath id="band-clip"><rect x="0" y="69" width="1078" height="629"/></clipPath>
      <radialGradient id="photo-tone" cx="50%" cy="40%" r="65%">
        <stop offset="0%" stop-color="#f1f1f1"/>
        <stop offset="100%" stop-color="#d6d6d6"/>
      </radialGradient>
    </defs>
    <rect class="band" x="0" y="69" width="1078" height="629" fill="var(--band)"/>
    <g clip-path="url(#band-clip)">
      <circle class="halo" cx="745" cy="385" r="314" fill="var(--halo)"/>
    </g>
    <path class="arc-thin" d="M745 113 A272 272 0 0 1 1017 385 L1005 385 A260 260 0 0 0 745 125 Z" fill="var(--ring-thin)"/>
    <path class="arc-light" d="M464 385 A281 281 0 0 0 745 666 L745 600 A215 215 0 0 1 530 385 Z" fill="var(--ring-light)"/>
    <circle class="ring" cx="745" cy="385" r="231" fill="none" stroke="var(--ring)" stroke-width="58"/>
    <g role="img" aria-label="Black and white photo of the two founders smiling at a meeting table">
      <circle cx="745" cy="385" r="203" fill="url(#photo-tone)"/>
    </g>
    <rect class="strip" x="0" y="675" width="1078" height="22" fill="var(--strip)"/>
    <rect class="logo-panel" x="751" y="586" width="327" height="176" fill="var(--paper)"/>
    <rect x="0" y="697" width="1078" height="65" fill="var(--paper)"/>
  </svg>

  <div class="contact">
    <div class="contact-title">Contact Us</div>
    <div class="contact-row">
      <svg viewBox="0 0 12 12"><path d="M6 0.5a4 4 0 0 0-4 4c0 3 4 7 4 7s4-4 4-7a4 4 0 0 0-4-4z" fill="var(--icon)"/><circle cx="6" cy="4.5" r="1.5" fill="#fff"/></svg>
      <div>TVA Limited<br>Harbourside House<br>Mill Lane, Kelbury, KB4 2RT</div>
    </div>
    <div class="contact-row tight">
      <svg viewBox="0 0 12 12"><circle cx="6" cy="6" r="6" fill="var(--icon)"/><path d="M4 3.2l1 1.6-.7.7c.4.9 1.1 1.6 2 2l.7-.7 1.6 1-.6 1c-2.4-.3-4.3-2.2-4.6-4.6z" fill="#fff"/></svg>
      <div>+44 (0) 1632 960214</div>
    </div>
    <div class="contact-row">
      <svg viewBox="0 0 12 12"><rect x="0.5" y="2.5" width="11" height="7.5" fill="var(--icon)"/><path d="M0.8 2.8L6 7l5.2-4.2" fill="none" stroke="#fff" stroke-width="0.9"/></svg>
      <div>hello@tollandvergeadvisory.com</div>
    </div>
  </div>

  <div class="web-link">www.tollandvergeadvisory.com</div>

  <div class="brand-name">Tolland Verge<br>Advisory</div>
</div>
</body>
</html>
```